Regional Consulting Business Needs a Business Card Design

We need a business card design for our new business based in Regional Victoria, Australia called Velor Power. We are a consulting company with our main goal being to save people momey money and reducing their carbon footprint. Anything from water saving showerheads, to energy saving lightglobes and even to solar power. We would like to see designs that use bright colours. The final design should shout 'we are here to help you'.

Industry/Entity Type

Business

```html
<!DOCTYPE html>
<html lang="en">
<head>
<meta charset="utf-8">
<title>Velor Power – Business Card</title>
<link rel="stylesheet" href="https://fonts.googleapis.com/css2?family=Arimo:wght@400;700&family=Open+Sans:wght@400;600&display=swap">
<style>
  :root {
    --page: #ecebe8;
    --card: #ffffff;
    --orange: #f6a01a;
    --orange-deep: #ef8f12;
    --yellow: #ffc414;
    --ink: #2b2b2b;
    --ink-soft: #555555;
    --grey-dark: #3a3a3a;
    --grey-mid: #9a9a9a;
    --grey-light: #d9d9d9;
  }
  * { box-sizing: border-box; margin: 0; padding: 0; }
  html, body { width: 1200px; height: 900px; overflow: hidden; }
  body {
    background: var(--page);
    position: relative;
    font-family: "Open Sans", Arial, sans-serif;
    color: var(--ink);
  }
  .card {
    position: absolute;
    width: 620px;
    height: 354px;
    background: var(--card);
    border-radius: 26px;
    overflow: hidden;
    box-shadow: 0 6px 18px rgba(0,0,0,0.18);
  }
  .card--back { left: 480px; top: 60px; }
  .card--front { left: 100px; top: 480px; }

  .brand {
    position: absolute;
    display: flex;
    align-items: center;
    gap: 12px;
  }
  .brand__mark {
    width: 34px;
    height: 34px;
    background: var(--orange);
    flex: none;
  }
  .brand__text { display: flex; flex-direction: column; }
  .brand__name {
    font-family: "Arimo", Arial, sans-serif;
    font-weight: 700;
    color: var(--grey-dark);
    font-size: 40px;
    line-height: 1;
  }
  .brand__tagline {
    font-family: "Arimo", Arial, sans-serif;
    font-weight: 700;
    font-size: 14px;
    color: var(--ink);
    margin-top: 4px;
  }
  .card--back .brand { left: 150px; top: 120px; }
  .card--front .brand { left: 150px; top: 26px; }
  .card--front .brand__name { font-size: 36px; }

  .back__decor {
    position: absolute;
    right: 0;
    top: 20px;
    width: 120px;
    height: 150px;
    background: linear-gradient(135deg, rgba(200,200,200,0.15), rgba(170,170,170,0.45) 55%, rgba(246,160,26,0.18));
  }
  .back__web {
    position: absolute;
    right: 44px;
    top: 236px;
    font-size: 18px;
    color: var(--ink);
  }

  .front__wave { position: absolute; inset: 0; width: 100%; height: 100%; }

  .person { position: absolute; left: 282px; top: 128px; }
  .person__name {
    font-family: "Arimo", Arial, sans-serif;
    font-size: 28px;
    color: var(--orange-deep);
    line-height: 1;
  }
  .person__role {
    font-family: "Arimo", Arial, sans-serif;
    font-size: 12.5px;
    letter-spacing: 0.3px;
    color: var(--ink-soft);
    margin-top: 7px;
    margin-left: 8px;
  }

  .contacts {
    position: absolute;
    left: 26px;
    top: 200px;
    list-style: none;
  }
  .contacts li {
    display: flex;
    align-items: center;
    gap: 10px;
    height: 25px;
    font-size: 15px;
    color: var(--ink);
  }
  .contacts svg { width: 16px; height: 16px; flex: none; }

  .address {
    position: absolute;
    left: 352px;
    top: 274px;
    font-family: "Arimo", Arial, sans-serif;
    font-size: 19px;
    line-height: 1.25;
    color: var(--ink);
    font-style: normal;
  }
</style>
</head>
<body>

  <section class="card card--back" aria-label="Card back">
    <div class="back__decor" role="img" aria-label="Faint stacked block decoration"></div>
    <div class="brand">
      <span class="brand__mark"></span>
      <div class="brand__text">
        <span class="brand__name">Velor Power</span>
        <span class="brand__tagline">Maintenance and consulting services</span>
      </div>
    </div>
    <p class="back__web">www.velorpower.com</p>
  </section>

  <section class="card card--front" aria-label="Card front">
    <svg class="front__wave" viewBox="0 0 620 354" preserveAspectRatio="none" aria-hidden="true">
      <defs>
        <linearGradient id="band-orange" x1="0" y1="0" x2="1" y2="0">
          <stop offset="0" stop-color="#f6a01a"/>
          <stop offset="0.45" stop-color="#ffc414"/>
          <stop offset="1" stop-color="#ef8f12"/>
        </linearGradient>
        <linearGradient id="band-grey" x1="0" y1="0" x2="1" y2="0">
          <stop offset="0" stop-color="#d9d9d9"/>
          <stop offset="0.5" stop-color="#9a9a9a"/>
          <stop offset="1" stop-color="#3a3a3a"/>
        </linearGradient>
      </defs>
      <path d="M0,138 C110,118 230,172 320,248 C410,302 530,300 620,270 L620,354 L0,354 Z" fill="url(#band-orange)"/>
      <path d="M40,118 C170,112 250,185 330,215 C420,255 540,262 620,215 L620,232 C540,282 410,278 320,234 C240,196 150,124 40,118 Z" fill="url(#band-grey)"/>
      <path d="M150,124 C230,140 270,188 330,222 C420,264 540,272 620,226" fill="none" stroke="#3a3a3a" stroke-width="3"/>
    </svg>

    <div class="brand">
      <span class="brand__mark"></span>
      <div class="brand__text">
        <span class="brand__name">Velor Power</span>
        <span class="brand__tagline">Maintenance and consulting services</span>
      </div>
    </div>

    <div class="person">
      <p class="person__name">Dana Whitlow</p>
      <p class="person__role">GENERAL MANAGER</p>
    </div>

    <ul class="contacts">
      <li>
        <svg viewBox="0 0 16 16" aria-label="Phone"><path d="M2,4 C2,2 4,2 5,2 L6,5 L4.5,6.5 C5.5,8.5 7.5,10.5 9.5,11.5 L11,10 L14,11 C14,12 14,14 12,14 C6,14 2,10 2,4 Z" fill="#2b2b2b"/></svg>
        <span>+61 3 5550 0182</span>
      </li>
      <li>
        <svg viewBox="0 0 16 16" aria-label="Mobile"><rect x="4" y="1" width="8" height="14" rx="1.5" fill="#2b2b2b"/><rect x="5.5" y="3" width="5" height="8" fill="#ffc414"/></svg>
        <span>+61 3 5550 0182</span>
      </li>
      <li>
        <svg viewBox="0 0 16 16" aria-label="Email"><rect x="1" y="3.5" width="14" height="9" fill="#2b2b2b"/><path d="M1.5,4 L8,9 L14.5,4" fill="none" stroke="#ffc414" stroke-width="1.2"/></svg>
        <span>info@velorpower.com</span>
      </li>
      <li>
        <svg viewBox="0 0 16 16" aria-label="Website"><circle cx="8" cy="8" r="6.5" fill="#2b2b2b"/><path d="M1.5,8 H14.5 M8,1.5 V14.5" stroke="#ffc414" stroke-width="1"/></svg>
        <span>www.velorpower.com</span>
      </li>
    </ul>

    <address class="address">Level 3, 48 Wattle Row.<br>North Ferncliff, Victoria 3352</address>
  </section>

</body>
</html>
```